依頼詳細
グランドオープンに合わせて4日間限定の来店者プレゼント企画を開催します。その告知として、新聞折り込みにチラシを入れようと思うます。今回はその、折り込み用チラシの作成をお願いいたします。プレゼント内容は5/29,30,31,6/1「プチシュープレゼント」各日50名限定となります。
記載項目
「グランドオープン」であること、「5/29,30、31,6/1各日 50名様限定スイーツプレゼント」があること(プレゼント内容の記載はしても、しなくてもどちらでもokです。)、店名ロゴ(添付)、〒371-0815 群馬県沼田市栄和町2871-5 TEL&FAX 0278-61-7350 CafeBookページ有♪
サイズ
B5
ページ数
片面
希望イメージ
シンプル 複雑
単色 カラフル
暗い 明るい
日常 高級
遊び心 厳粛
未来的 伝統的
女性的 男性的
希望する色
緑 青
納品ファイル
• 高解像度JPG (.jpg)
補足説明
プレゼント内容の変更。
5/29,30 プチシュー 各日限定50個
5/31,6/1 いちごミルクプリン 各日限定50個 となります。
ロゴファイル追加です

自店のcolorにとてもあっていたから
シンプルなのにインパクトが大きく目を引く配色だったため

色々なデザインを頂きありがとうございました。自分ではなかなか出てこない案が多くロゴの時も感じましたが、とてもいい刺激になりました。
ありがとうございました。

```html
<!DOCTYPE html>
<html lang="ja">
<head>
<meta charset="utf-8">
<title>グランドオープン｜Sweets &amp; Cafe こもれび</title>
<link rel="stylesheet" href="https://fonts.googleapis.com/css2?family=Kosugi+Maru&family=M+PLUS+Rounded+1c:wght@400;700;800&family=Zen+Maru+Gothic:wght@500;700&display=swap">
<style>
  :root {
    --cream: #f6f1e2;
    --stripe: #ebe3c9;
    --paper: #fffdf6;
    --green: #7ab33b;
    --green-dark: #5b8f23;
    --brown: #5e4a2e;
    --text: #4a3d2a;
    --orange: #ef8a1e;
    --pink: #e86c8a;
    --blue: #4fa2d8;
    --map: #a9cf6f;
  }
  * { margin: 0; padding: 0; box-sizing: border-box; }
  html, body { width: 867px; height: 1200px; overflow: hidden; }
  body {
    background: repeating-linear-gradient(90deg, var(--cream) 0 22px, var(--stripe) 22px 44px);
    font-family: "Zen Maru Gothic", "Kosugi Maru", sans-serif;
    color: var(--text);
    position: relative;
  }
  .flyer { position: absolute; inset: 0; }
  .flyer * { white-space: nowrap; }
  .header {
    position: absolute; left: 0; top: 0; width: 867px; height: 262px;
    background: var(--paper);
  }
  .title {
    position: absolute; left: 36px; top: 92px;
    font-family: "M PLUS Rounded 1c", sans-serif; font-weight: 400;
    font-size: 80px; letter-spacing: 0; color: var(--brown); line-height: 1;
  }
  .tagline {
    position: absolute; left: 40px; top: 200px;
    font-size: 24px; font-weight: 700; color: var(--brown);
  }
  .date-badge {
    position: absolute; left: 694px; top: 30px; width: 160px; height: 160px;
    border-radius: 50%; background: var(--green); color: #fff;
    text-align: center; font-family: "M PLUS Rounded 1c", sans-serif; font-weight: 800;
  }
  .date-badge .month { position: absolute; left: 26px; top: 20px; font-size: 30px; line-height: 1; }
  .date-badge .day { position: absolute; left: 50px; top: 48px; font-size: 62px; line-height: 1; }
  .date-badge .dow { position: absolute; right: 10px; top: 66px; font-size: 16px; background: #fff; color: var(--green); border-radius: 50%; width: 26px; height: 26px; line-height: 26px; }
  .date-badge .time { position: absolute; left: 0; right: 0; top: 116px; font-size: 24px; line-height: 1; }

  .brand {
    position: absolute; left: 0; right: 0; top: 320px; text-align: center;
    font-family: "M PLUS Rounded 1c", sans-serif; font-weight: 800; color: var(--green);
  }
  .brand .sub { font-size: 48px; line-height: 1; }
  .brand .name { font-size: 92px; line-height: 1.15; display: inline-flex; align-items: center; gap: 18px; }
  .brand .name::after { content: ""; width: 40px; height: 40px; border-radius: 50%; background: var(--green); }

  .about {
    position: absolute; left: 0; right: 0; top: 560px; text-align: center;
    font-size: 22px; line-height: 1.55; font-weight: 500; color: var(--text);
  }

  .present { position: absolute; left: 0; width: 867px; top: 672px; height: 320px; background: var(--paper); }
  .present h2 {
    position: absolute; left: 60px; top: 14px;
    font-family: "M PLUS Rounded 1c", sans-serif; font-weight: 800; font-size: 46px; color: var(--green);
  }
  .present .lead { position: absolute; left: 64px; top: 78px; font-size: 22px; font-weight: 700; color: var(--text); }
  .offer { position: absolute; left: 64px; display: flex; align-items: center; gap: 10px; }
  .offer.first { top: 122px; }
  .offer.second { top: 212px; }
  .day-dot {
    width: 64px; height: 64px; border-radius: 50%; color: #fff; text-align: center;
    font-family: "M PLUS Rounded 1c", sans-serif; font-weight: 800; line-height: 1;
    display: flex; flex-direction: column; justify-content: center;
  }
  .day-dot small { font-size: 14px; }
  .day-dot b { font-size: 30px; }
  .day-dot.may { background: var(--pink); }
  .day-dot.jun { background: var(--blue); }
  .offer .item {
    margin-left: 20px; font-family: "M PLUS Rounded 1c", sans-serif; font-weight: 800;
    font-size: 54px; color: var(--brown);
  }
  .limit-badge {
    position: absolute; left: 620px; top: 80px; width: 150px; height: 150px; border-radius: 50%;
    background: var(--orange); color: #fff; text-align: center;
    display: flex; flex-direction: column; justify-content: center;
    font-weight: 700; font-size: 20px; line-height: 1.3;
  }

  .contact { position: absolute; left: 46px; top: 1010px; color: var(--text); }
  .contact .sns { font-family: "M PLUS Rounded 1c", sans-serif; font-weight: 800; font-size: 30px; color: var(--green-dark); }
  .contact .sns span { font-size: 24px; }
  .contact p { font-size: 20px; font-weight: 700; margin-top: 6px; }
  .contact .tel { font-size: 40px; font-family: "M PLUS Rounded 1c", sans-serif; font-weight: 800; color: var(--brown); margin-top: 0; }
  .contact .tel .label { font-size: 26px; }
  .contact .parking::before { content: "P"; display: inline-block; width: 22px; height: 22px; line-height: 22px; text-align: center; background: var(--blue); color: #fff; border-radius: 3px; margin-right: 6px; }
  .map {
    position: absolute; left: 520px; top: 1000px; width: 320px; height: 180px;
    border-radius: 60px 90px 40px 100px; background: var(--map);
  }
</style>
</head>
<body>
<main class="flyer">
  <header class="header">
    <h1 class="title">グランドオープン</h1>
    <p class="tagline">この町にフレーバーteaと焼き菓子のカフェができました</p>
    <div class="date-badge">
      <span class="month">5月</span>
      <span class="day">29</span>
      <span class="dow">木</span>
      <span class="time">AM10:00</span>
    </div>
  </header>

  <div class="brand">
    <div class="sub">Sweets &amp; Cafe</div>
    <div class="name">こもれび</div>
  </div>

  <p class="about">北欧をイメージしたナチュラルなカフェです。<br>大きな窓＆高い天井による明るく開放的な空間で<br>あなただけの小さな幸せをたくさんみつけてください</p>

  <section class="present">
    <h2>Special Sweets Present</h2>
    <p class="lead">ご来店のお客様にプレゼントをご用意しました。</p>
    <div class="offer first">
      <div class="day-dot may"><small>5月</small><b>29</b></div>
      <div class="day-dot may"><small>5月</small><b>30</b></div>
      <span class="item">プチシュー</span>
    </div>
    <div class="offer second">
      <div class="day-dot may"><small>5月</small><b>31</b></div>
      <div class="day-dot jun"><small>6月</small><b>1</b></div>
      <span class="item">いちごミルクプリン</span>
    </div>
    <div class="limit-badge">各日<br>限定50個<br>プレゼント!</div>
  </section>

  <footer class="contact">
    <div class="sns">CafeBook <span>ページあります!</span></div>
    <p>〒371-0815　群馬県沼田市栄和町2871-5</p>
    <p class="tel"><span class="label">TEL &amp; FAX</span> 0278-61-7350</p>
    <p class="parking">8台ご用意しました!</p>
  </footer>
  <div class="map" role="img" aria-label="店舗周辺の案内地図"></div>
</main>
</body>
</html>
```